SunGrove Yoga Website Design

Business Logo - attached
5 pages being:
Home
About
Classes
Blog
Contact

Would like Scrolling webpage and yoga symbols to be used.

Must have's being:
Easy to navigate, Text needs to be able to be edited/updated, Enquire Now Links, More Information Links, be a secure site, SEO,

Please refer to attached document for the information for the body of the website.

Target Market(s)

Educators, Community Service, Health and Wellbeing, Mental Health

Industry/Entity Type

Yoga

Coding

Coded - Design and coding required

Number of Pages Required

5+ page

Font styles to use
Other font styles liked:
• Bella Bold BC

Colors
0094D4
00A9DD
6FCCEA
C7EBF8
E9F6FB
6B429C
8869AF
B7A5CE
E3DAEB
F3F0F8

Requirements
Must have
• Easy to navigate, Text needs to be able to be edited/updated, Enquire Now Links, More Information Links, be a secure site, SEO,
Nice to have
• Scrolling webpage, yoga symbols

```html
<!DOCTYPE html>
<html lang="en">
<head>
<meta charset="utf-8">
<title>SunGrove Yoga</title>
<link rel="stylesheet" href="https://fonts.googleapis.com/css2?family=Montserrat:wght@400;500;600;700&family=Kaushan+Script&display=swap">
<style>
:root{
  --blue-deep:#0094D4;
  --blue:#00A9DD;
  --blue-mid:#6FCCEA;
  --blue-soft:#C7EBF8;
  --blue-pale:#E9F6FB;
  --purple:#6B429C;
  --purple-mid:#8869AF;
  --purple-soft:#B7A5CE;
  --purple-pale:#E3DAEB;
  --lilac:#F3F0F8;
  --ink:#1d1530;
  --text:#555;
  --line:#d9d4e2;
  --footer:#262429;
}
*{box-sizing:border-box;margin:0;padding:0}
html,body{width:1200px;height:3997px;overflow:hidden;background:#fff}
body{position:relative;font-family:'Montserrat',sans-serif;color:var(--text)}
.abs{position:absolute}
.script{font-family:'Kaushan Script',cursive;font-weight:400}
.btn{position:absolute;display:flex;align-items:center;justify-content:center;border-radius:22px;color:#fff;font-size:13px;font-weight:600;text-decoration:none}
.btn-purple{background:var(--purple)}
.btn-blue{background:var(--blue)}

/* header */
.brand{position:absolute;left:108px;top:22px;display:flex;align-items:center;gap:8px;color:var(--purple);font-size:13px;font-weight:600}
.brand-dot{width:26px;height:26px;border-radius:50%;background:var(--purple-pale)}
.nav{position:absolute;top:28px;left:554px}
.nav a{position:absolute;font-size:13px;font-weight:600;color:var(--ink);text-decoration:none;white-space:nowrap}

/* hero */
.hero-title-top{left:106px;top:165px;font-size:52px;color:var(--purple);line-height:1;z-index:2}
.hero-title{left:104px;top:232px;font-size:74px;line-height:1.1;white-space:nowrap;z-index:2}
.hero-title .b{color:var(--blue)}
.hero-title .y{color:var(--purple)}
.hero-copy{left:106px;top:378px;width:500px;font-size:13px;line-height:27px}
.photo{position:absolute;border-radius:50% 50% 46% 46%/55% 55% 40% 40%}
.photo-hero{left:690px;top:112px;width:412px;height:438px;background:radial-gradient(ellipse at 50% 40%,var(--blue-soft) 0%,var(--blue-pale) 55%,#fff 75%),#fff}
.shadow-ellipse{position:absolute;border-radius:50%;background:var(--purple-pale)}

/* stats */
.stats{left:0;top:672px;width:1200px;height:169px;background:var(--lilac)}
.stat{position:absolute;top:38px}
.stat-num{font-size:48px;font-weight:700;color:var(--ink);line-height:1.1}
.stat-label{margin-top:6px;font-size:13px;color:var(--purple-mid);letter-spacing:.3px}

/* about */
.photo-side{width:412px;height:346px;background:radial-gradient(ellipse at 50% 45%,var(--blue-soft) 0%,var(--blue-pale) 55%,#fff 78%)}
.section-title{font-size:40px;color:var(--purple);line-height:1.2;white-space:nowrap}
.section-title .b{color:var(--blue)}
.about-copy{left:608px;top:1032px;width:490px;font-size:13px;line-height:27px}

/* benefits */
.center{left:0;width:1200px;text-align:center}
.benefits-copy{top:1443px;font-size:13px;line-height:27px}
.benefit{position:absolute;top:1544px;width:320px}
.benefit-icon{width:76px;height:78px;border-radius:12px;background:linear-gradient(135deg,var(--blue-pale),var(--blue-soft))}
.benefit h3{margin-top:28px;font-size:22px;line-height:1.2;font-weight:600;color:var(--purple)}
.benefit ul{list-style:none;margin-top:14px}
.benefit li{font-size:12.5px;line-height:34px;white-space:nowrap}
.benefit li::before{content:"· "}

/* newsletter */
.newsletter{left:106px;top:1977px;width:988px;height:255px;border-radius:30px;background:var(--purple)}
.newsletter h2{position:absolute;left:83px;top:44px;font-size:32px;color:#fff}
.newsletter p{position:absolute;left:83px;top:102px;width:830px;font-size:12.5px;line-height:27px;color:#efe9f7}
.news-input{position:absolute;left:83px;top:169px;width:707px;height:41px;background:#fff;border-radius:4px 0 0 4px;padding-left:30px;display:flex;align-items:center;font-size:12.5px;color:#aaa}
.news-btn{position:absolute;left:790px;top:169px;width:114px;height:41px;background:var(--blue);border-radius:0 4px 4px 0;color:#fff;font-size:13px;font-weight:600;display:flex;align-items:center;justify-content:center}

/* blog */
.card{position:absolute;top:2385px;width:322px;height:409px;border:1.5px solid var(--line);border-radius:12px}
.card-img{position:absolute;left:30px;top:25px;width:262px;height:140px;border-radius:10px}
.card-date{position:absolute;left:30px;top:177px;padding:3px 8px;border-radius:10px;background:var(--purple);color:#fff;font-size:10px}
.card h3{position:absolute;left:30px;top:210px;width:270px;font-size:19px;line-height:26px;font-weight:600;color:var(--ink)}
.card p{position:absolute;left:30px;top:275px;width:262px;font-size:11.5px;line-height:21px;color:#444}
.card a{position:absolute;left:30px;top:370px;font-size:13px;color:var(--purple);text-decoration:none}

/* contact */
.contact-copy{top:3003px;font-size:13px;line-height:27px}
.form{left:605px;top:3081px;width:489px;height:554px;border:1.5px solid var(--line);border-radius:14px}
.label{position:absolute;left:47px;font-size:12.5px;color:#555}
.field{position:absolute;left:47px;width:393px;height:39px;border:1px solid #bbb;border-radius:4px}
.form-btn{position:absolute;left:47px;width:393px;height:39px;border-radius:3px;color:#fff;font-size:13px;font-weight:600;display:flex;align-items:center;justify-content:center}

/* footer */
.footer{left:0;top:3700px;width:1200px;height:297px}
.footer-brand{position:absolute;left:0;width:1200px;top:3808px;color:#fff;font-size:16px;font-weight:600;display:flex;justify-content:center;align-items:center;gap:10px}
.footer-brand .dot{width:22px;height:22px;border-radius:50%;background:var(--purple-mid)}
.social{position:absolute;top:3897px;width:36px;height:36px;border-radius:50%;border:2px solid #fff}
.footer-rule{left:0;top:3952px;width:1200px;height:1px;background:#5a5860}
.footer-text{top:3968px;font-size:13px;color:#ddd}
</style>
</head>
<body>

<header>
  <div class="brand"><span class="brand-dot"></span>SunGrove Yoga</div>
  <nav class="nav">
    <a style="left:0">Home</a>
    <a style="left:73px">About</a>
    <a style="left:155px">Classes</a>
    <a style="left:248px">Blog</a>
    <a style="left:318px">Contact</a>
  </nav>
  <a class="btn btn-purple" style="left:965px;top:16px;width:128px;height:41px">Enquire Now</a>
</header>

<section class="hero">
  <div class="shadow-ellipse" style="left:690px;top:512px;width:412px;height:34px"></div>
  <div class="photo photo-hero" role="img" aria-label="Woman in a forearm scorpion yoga pose on a mat"></div>
  <div class="abs script hero-title-top">Welcome to</div>
  <div class="abs script hero-title"><span class="b">SunGrove</span> <span class="y">Yoga...</span></div>
  <p class="abs hero-copy">SunGrove Yoga believe that you are never too young to benefit from and fall in love with yoga. My aim is to EMPOWER kids and teens to thrive by teaching life skills in Yoga.</p>
  <a class="btn btn-purple" style="left:106px;top:478px;width:128px;height:40px">Enquire Now</a>
  <a class="btn btn-blue" style="left:253px;top:478px;width:127px;height:40px">Learn More</a>
</section>

<section class="abs stats">
  <div class="stat" style="left:106px"><div class="stat-num">1000+</div><div class="stat-label">HAPPY CUSTOMERS</div></div>
  <div class="stat" style="left:386px"><div class="stat-num">20+</div><div class="stat-label">YEARS EXPERIENCE</div></div>
  <div class="stat" style="left:667px"><div class="stat-num">331+</div><div class="stat-label">ONLINE RATINGS</div></div>
  <div class="stat" style="left:920px"><div class="stat-num">33145+</div><div class="stat-label">TOTAL CLIENTS</div></div>
</section>

<section class="about">
  <div class="shadow-ellipse" style="left:98px;top:1245px;width:412px;height:36px"></div>
  <div class="photo photo-side" style="left:98px;top:928px" role="img" aria-label="Woman seated cross-legged in a meditation pose"></div>
  <h2 class="abs script section-title" style="left:608px;top:958px">About <span class="b">SunGrove</span></h2>
  <p class="abs about-copy">SunGrove Yoga gives kids an opportunity to enjoy and experience yoga for themselves and primarily focuses on programs for Schools, Pre Schools and Early Learning Centres, Private Classes, Sporting Clubs, Martial Arts Schools, Scout Groups and Occupational Therapy Centres just to name a few. All classes are age appropriate and encourage children's natural drive to learn, move, and be creative.</p>
  <a class="btn btn-blue" style="left:608px;top:1211px;width:127px;height:40px">Learn More</a>
</section>

<section class="benefits">
  <h2 class="abs script section-title center" style="top:1368px"><span class="b">Benefits</span> of Yoga...</h2>
  <p class="abs center benefits-copy">The benefits of yoga can last a lifetime. It is my aim &amp; passion to introduce yoga to kids of all ages and backgrounds so<br>that they can not only experience the benefits of yoga but fall in love with the practice.<br>Yoga benefits include:</p>

  <div class="benefit" style="left:106px">
    <div class="benefit-icon" role="img" aria-label="Line icon of a toned torso"></div>
    <h3>Healthy Bodies</h3>
    <ul>
      <li>Develops strong, flexible and healthy bodies</li>
      <li>Promotes spinal alignment and good posture</li>
      <li>Builds energy and stamina</li>
      <li>Helps breathing and lung capacity</li>
    </ul>
  </div>
  <div class="benefit" style="left:439px">
    <div class="benefit-icon" role="img" aria-label="Line icon of a calm mind"></div>
    <h3>Healthy Minds</h3>
    <ul>
      <li>Cultivates confidence and self-esteem</li>
      <li>Develops concentration and attention</li>
      <li>Helps relax and sleep better</li>
      <li>Calms the nervous system</li>
    </ul>
  </div>
  <div class="benefit" style="left:771px">
    <div class="benefit-icon" role="img" aria-label="Line icon of a figure meditating on a lotus"></div>
    <h3>Healthy Spirits</h3>
    <ul>
      <li>Cultivates kindness to themselves and others</li>
      <li>Builds balance and inner quiet</li>
      <li>Fosters creativity, expression and imagination</li>
      <li>Focuses on positive self-talk</li>
    </ul>
  </div>
  <a class="btn btn-purple" style="left:463px;top:1847px;width:128px;height:40px">Enquire Now</a>
  <a class="btn btn-blue" style="left:610px;top:1847px;width:127px;height:40px">Learn More</a>
</section>

<section class="abs newsletter">
  <h2 class="script">Subscribe Our Newsletter</h2>
  <p>Lorem ipsum dolor sit amet consectetur. Pellentesque magna consequat sagittis dui ac urna arcu sociis eu. Lacinia &nbsp;orci a posuere sed diam vulputate tincidunt. Ut enim tortor quis risus donec nunc.</p>
  <div class="news-input">Enter your Email Address</div>
  <div class="news-btn">Subscribe</div>
</section>

<section class="blog">
  <h2 class="abs script section-title" style="left:104px;top:2318px;font-size:36px">Our blogs</h2>
  <article class="card" style="left:106px">
    <div class="card-img" role="img" aria-label="Close-up of a person meditating cross-legged" style="background:linear-gradient(135deg,#b89a86,#e9e4df)"></div>
    <span class="card-date">5 Th May, 2019</span>
    <h3>At vero eos et accusamus et iusto odio dignissimos</h3>
    <p>ducimus qui blanditiis praesentium voluptatum deleniti atque corrupti quos dolores et quas molestias excepturi sint occaecati cupiditate</p>
    <a>Read More →</a>
  </article>
  <article class="card" style="left:439px">
    <div class="card-img" role="img" aria-label="Person balancing in tree pose in a living room" style="background:linear-gradient(135deg,#8a6a4c,#d8d6d2)"></div>
    <span class="card-date">5 Th May, 2019</span>
    <h3>At vero eos et accusamus et iusto odio dignissimos</h3>
    <p>ducimus qui blanditiis praesentium voluptatum deleniti atque corrupti quos dolores et quas molestias excepturi sint occaecati cupiditate</p>
    <a>Read More →</a>
  </article>
  <article class="card" style="left:771px">
    <div class="card-img" role="img" aria-label="Three children doing yoga with arms raised" style="background:linear-gradient(135deg,#e8e2df,#c9b6d4)"></div>
    <span class="card-date">5 Th May, 2019</span>
    <h3>At vero eos et accusamus et iusto odio dignissimos</h3>
    <p>ducimus qui blanditiis praesentium voluptatum deleniti atque corrupti quos dolores et quas molestias excepturi sint occaecati cupiditate</p>
    <a>Read More →</a>
  </article>
  <a class="btn btn-blue" style="left:536px;top:2815px;width:127px;height:41px">Learn More</a>
</section>

<section class="contact">
  <h2 class="abs script section-title center" style="top:2945px;font-size:36px">Find Out More...</h2>
  <p class="abs center contact-copy">If you would like any further information or simply need clarification, please send me an email and I<br>will happily answer your questions either via email or over the phone if you prefer.</p>
  <div class="shadow-ellipse" style="left:98px;top:3500px;width:412px;height:36px"></div>
  <div class="photo photo-side" style="left:98px;top:3135px;height:390px" role="img" aria-label="Man seated cross-legged in meditation"></div>

  <form class="abs form">
    <span class="label" style="top:30px">Name*</span>
    <div class="field" style="top:51px"></div>
    <span class="label" style="top:106px">Email*</span>
    <div class="field" style="top:127px"></div>
    <span class="label" style="top:182px">Subject*</span>
    <div class="field" style="top:203px"></div>
    <span class="label" style="top:258px">Message*</span>
    <div class="field" style="top:278px;height:114px"></div>
    <div class="form-btn" style="top:405px;background:var(--purple)">Send</div>
    <span class="abs" style="left:0;width:486px;text-align:center;top:449px;font-size:12px;color:#777">Or</span>
    <div class="form-btn" style="top:473px;background:var(--blue)">Call Hannah 0400 555 018</div>
  </form>
</section>

<footer>
  <svg class="abs footer" viewBox="0 0 1200 297" preserveAspectRatio="none" aria-hidden="true">
    <defs>
      <linearGradient id="edge" x1="0" x2="1">
        <stop offset="0" stop-color="#6B429C"/>
        <stop offset="1" stop-color="#00A9DD"/>
      </linearGradient>
    </defs>
    <path d="M0 50 C150 20 260 90 420 75 C600 58 700 40 850 55 C1000 70 1100 20 1200 0 L1200 297 L0 297 Z" fill="#262429"/>
    <path d="M0 50 C150 20 260 90 420 75 C600 58 700 40 850 55 C1000 70 1100 20 1200 0" fill="none" stroke="url(#edge)" stroke-width="8"/>
  </svg>
  <div class="footer-brand"><span class="dot"></span>SunGrove Yoga</div>
  <a class="social" style="left:553px" aria-label="Social profile one"></a>
  <a class="social" style="left:610px" aria-label="Social profile two"></a>
  <div class="abs footer-rule"></div>
  <p class="abs footer-text" style="left:111px">Copyright 2023 SunGrove Yoga</p>
  <p class="abs footer-text" style="left:880px;display:flex;align-items:center;gap:8px">
    <svg width="18" height="13" viewBox="0 0 18 13" aria-hidden="true"><rect x="0" y="0" width="18" height="13" rx="1.5" fill="#fff"/><path d="M1 1.5 L9 7.5 L17 1.5" fill="none" stroke="#262429" stroke-width="1.5"/></svg>
    hello@sungroveyoga.example
  </p>
</footer>

</body>
</html>
```